" O Perito nomeado pelo Juiz do Trabalho agenda uma Perícia Trabalhista, pedindo para avaliar a Insalubridade ou Periculosidade que o Reclamante afirma existir, tanto o Reclamante como a Reclamada tem o direito de contratar um Assistente Técnico, é ai que entra o nosso serviço. site: www.rotaverdeassessoria.com "

```html
<!DOCTYPE html>
<html lang="pt-BR">
<head>
<meta charset="utf-8">
<title>Rota Verde Assessoria – Cartão de visita</title>
<link href="https://fonts.googleapis.com/css2?family=Montserrat:wght@300;400;500&display=swap" rel="stylesheet">
<style>
  :root {
    --page-bg: #e6e4e1;
    --card-dark: #5b5b5c;
    --card-darker: #4a4a4b;
    --card-light: #ffffff;
    --ink-light: #f2f2f2;
    --ink-dark: #3a3a3b;
    --ink-muted: #6d6d6e;
  }
  * { margin: 0; padding: 0; box-sizing: border-box; }
  html, body { width: 1200px; height: 1200px; overflow: hidden; }
  body {
    background: var(--page-bg);
    font-family: "Montserrat", sans-serif;
    position: relative;
  }
  .card {
    position: absolute;
    left: 180px;
    width: 840px;
    height: 480px;
    box-shadow: 0 10px 30px rgba(0,0,0,.18);
    overflow: hidden;
  }
  .card--back { top: 80px; background: var(--card-light); }
  .card--front { top: 640px; background: var(--card-dark); }

  /* wordmark */
  .wordmark { display: flex; align-items: center; gap: 18px; }
  .wordmark__square { width: 34px; height: 34px; }
  .wordmark__text { display: flex; flex-direction: column; }
  .wordmark__name {
    font-weight: 400;
    font-size: 40px;
    letter-spacing: 5px;
    text-transform: uppercase;
    line-height: 1;
  }
  .wordmark__tag {
    font-weight: 400;
    font-size: 12px;
    letter-spacing: 9px;
    text-transform: uppercase;
    text-align: right;
    margin-top: 8px;
    padding-top: 8px;
    border-top: 1.5px solid currentColor;
  }
  .card--front .wordmark {
    position: absolute; left: 50%; top: 50%;
    transform: translate(-50%, -50%);
    color: var(--ink-light);
  }
  .card--front .wordmark__square { background: var(--ink-light); }

  /* back */
  .card__band { position: absolute; inset: 0; }
  .card--back .wordmark {
    position: absolute; left: 56px; top: 56px;
    color: var(--ink-dark);
  }
  .card--back .wordmark__square { background: var(--ink-dark); width: 24px; height: 24px; }
  .card--back .wordmark__name { font-size: 24px; letter-spacing: 3px; }
  .card--back .wordmark__tag { font-size: 8px; letter-spacing: 6px; margin-top: 5px; padding-top: 5px; }
  .card__mark {
    position: absolute; left: 120px; bottom: 90px;
    width: 110px; height: 110px;
    background: var(--card-darker);
  }
  .contact {
    position: absolute; right: 52px; top: 140px;
    list-style: none;
    display: flex; flex-direction: column; gap: 26px;
    color: var(--ink-muted);
    font-size: 14px; font-weight: 400; line-height: 1.5;
    text-align: right;
  }
  .contact__item { display: flex; align-items: center; justify-content: flex-end; gap: 18px; }
  .contact__icon { width: 20px; height: 20px; flex: none; fill: var(--ink-dark); }
</style>
</head>
<body>

<section class="card card--back" aria-label="Verso do cartão">
  <svg class="card__band" viewBox="0 0 840 480" preserveAspectRatio="none" aria-hidden="true">
    <polygon points="0,190 560,480 0,480" fill="var(--card-dark)"/>
  </svg>
  <div class="card__mark" aria-hidden="true"></div>

  <div class="wordmark">
    <span class="wordmark__square" aria-hidden="true"></span>
    <div class="wordmark__text">
      <span class="wordmark__name">Rota Verde</span>
      <span class="wordmark__tag">Assessoria</span>
    </div>
  </div>

  <ul class="contact">
    <li class="contact__item">
      <span>Rua das Palmeiras, 240<br>5º andar – Centro – Campinas/SP</span>
      <svg class="contact__icon" viewBox="0 0 24 24" aria-hidden="true"><path d="M12 2a7 7 0 0 0-7 7c0 5.2 7 13 7 13s7-7.8 7-13a7 7 0 0 0-7-7zm0 9.5A2.5 2.5 0 1 1 12 6.5a2.5 2.5 0 0 1 0 5z"/></svg>
    </li>
    <li class="contact__item">
      <span>www.rotaverdeassessoria.com</span>
      <svg class="contact__icon" viewBox="0 0 24 24" aria-hidden="true"><path d="M12 2a10 10 0 1 0 0 20 10 10 0 0 0 0-20zm6.9 9h-3a15 15 0 0 0-1.3-5.6A8 8 0 0 1 18.9 11zM12 4.1c.9 1.3 1.8 3.7 1.9 6.9h-3.8c.1-3.2 1-5.6 1.9-6.9zM9.4 5.4A15 15 0 0 0 8.1 11h-3a8 8 0 0 1 4.3-5.6zM5.1 13h3a15 15 0 0 0 1.3 5.6A8 8 0 0 1 5.1 13zm6.9 6.9c-.9-1.3-1.8-3.7-1.9-6.9h3.8c-.1 3.2-1 5.6-1.9 6.9zm2.6-1.3a15 15 0 0 0 1.3-5.6h3a8 8 0 0 1-4.3 5.6z"/></svg>
    </li>
    <li class="contact__item">
      <span>contato@rotaverdeassessoria.com.br</span>
      <svg class="contact__icon" viewBox="0 0 24 24" aria-hidden="true"><path d="M3 5h18v14H3zm2 2v.5l7 5 7-5V7zm0 3v7h14v-7l-7 5z"/></svg>
    </li>
    <li class="contact__item">
      <span>11 3040-2715<br>11 98125-4630</span>
      <svg class="contact__icon" viewBox="0 0 24 24" aria-hidden="true"><path d="M6.6 10.8a15 15 0 0 0 6.6 6.6l2.2-2.2a1 1 0 0 1 1-.25 11.4 11.4 0 0 0 3.6.6 1 1 0 0 1 1 1V20a1 1 0 0 1-1 1A17 17 0 0 1 3 4a1 1 0 0 1 1-1h3.5a1 1 0 0 1 1 1c0 1.25.2 2.45.6 3.6a1 1 0 0 1-.25 1z"/></svg>
    </li>
  </ul>
</section>

<section class="card card--front" aria-label="Frente do cartão">
  <div class="wordmark">
    <span class="wordmark__square" aria-hidden="true"></span>
    <div class="wordmark__text">
      <span class="wordmark__name">Rota Verde</span>
      <span class="wordmark__tag">Assessoria</span>
    </div>
  </div>
</section>

</body>
</html>
```